Business card

A basic business card using the new logo
The logo has our address on it is all I need is onset with the following

Dale Whitford
Manager of Sales and Service

Cell 508-731-2286

Email dw71846@mailbrook.net

Next card

Neil Ostrand
Manager

Cell 978-215-3907

Email nostrand7@qx.net

```html
<!DOCTYPE html>
<html lang="en">
<head>
<meta charset="utf-8">
<title>Northgate Transit Systems – Business Card</title>
<link rel="stylesheet" href="https://fonts.googleapis.com/css2?family=Cinzel:wght@500&family=Quicksand:wght@400;500;700&display=swap">
<style>
  :root {
    --backdrop: #e4e2df;
    --card-front: #f3f3f3;
    --card-back: #3a3a3a;
    --brand-blue: #2a8fd1;
    --ink: #2b2b2b;
    --ink-soft: #555555;
    --ink-light: #d9d9d9;
  }
  html, body {
    margin: 0;
    width: 1200px;
    height: 900px;
    overflow: hidden;
    background: var(--backdrop);
  }
  .canvas {
    position: relative;
    width: 1200px;
    height: 900px;
  }
  .card {
    position: absolute;
    left: 285px;
    width: 630px;
    height: 360px;
    box-shadow: 0 6px 18px rgba(0,0,0,0.18);
    font-family: "Quicksand", sans-serif;
  }
  .card--front { top: 70px; background: var(--card-front); }
  .card--back  { top: 490px; background: var(--card-back); }

  .contact {
    position: absolute;
    left: 56px;
    top: 108px;
  }
  .contact__name {
    font-family: "Cinzel", serif;
    font-weight: 500;
    font-size: 21px;
    letter-spacing: 2px;
    color: var(--ink);
    margin: 0;
  }
  .contact__title {
    font-size: 14px;
    font-weight: 500;
    letter-spacing: 1.6px;
    color: var(--brand-blue);
    margin: 6px 0 18px;
  }
  .contact__row {
    display: flex;
    align-items: center;
    gap: 12px;
    font-size: 14px;
    letter-spacing: 1.2px;
    color: var(--ink-soft);
    margin-bottom: 10px;
  }
  .contact__icon { width: 14px; height: 14px; flex: none; }

  .brand {
    position: absolute;
    text-align: left;
  }
  .card--front .brand { left: 350px; top: 130px; }
  .card--back .brand { left: 50%; top: 50%; transform: translate(-50%, -50%); }
  .brand__name {
    font-size: 44px;
    font-weight: 700;
    color: var(--brand-blue);
    line-height: 1;
    margin: 0 0 8px;
  }
  .brand__legal,
  .brand__address {
    font-size: 12px;
    font-weight: 500;
    color: var(--ink);
    margin: 0;
    line-height: 1.35;
  }
  .brand__address { display: flex; align-items: center; gap: 6px; }
  .brand__dot {
    width: 9px; height: 9px; border-radius: 50%;
    background: var(--brand-blue);
  }
  .card--back .brand__legal,
  .card--back .brand__address { color: var(--ink-light); }
</style>
</head>
<body>
<main class="canvas">
  <section class="card card--front">
    <div class="contact">
      <h1 class="contact__name">Dale Whitford</h1>
      <p class="contact__title">Manager of Sales and Service</p>
      <div class="contact__row">
        <svg class="contact__icon" viewBox="0 0 16 16" aria-hidden="true">
          <path d="M2 5c0-2 2-3 6-3s6 1 6 3l-3 1-1-2H6L5 6z M4 8h8l1 6H3z" fill="none" stroke="#2a8fd1" stroke-width="1.4" stroke-linejoin="round"/>
        </svg>
        <span>508-731-2286</span>
      </div>
      <div class="contact__row">
        <svg class="contact__icon" viewBox="0 0 16 16" aria-hidden="true">
          <rect x="1.5" y="3.5" width="13" height="9" fill="none" stroke="#2a8fd1" stroke-width="1.4"/>
          <path d="M1.5 3.5 8 9l6.5-5.5" fill="none" stroke="#2a8fd1" stroke-width="1.4"/>
        </svg>
        <span>dw71846@mailbrook.net</span>
      </div>
    </div>
    <div class="brand">
      <p class="brand__name">Northgate</p>
      <p class="brand__legal">Northgate Transit Systems, LLC</p>
      <p class="brand__address"><span class="brand__dot"></span>18 Larkspur Ln Hollis MA 01742</p>
    </div>
  </section>

  <section class="card card--back">
    <div class="brand">
      <p class="brand__name">Northgate</p>
      <p class="brand__legal">Northgate Transit Systems, LLC</p>
      <p class="brand__address"><span class="brand__dot"></span>18 Larkspur Ln Hollis MA 01742</p>
    </div>
  </section>
</main>
</body>
</html>
```